Harbor Lodge Sign for the road

Design an 8'x8' vector sign for the Harbor Lodge. The sign can only use two solid colors plus white. Use red, white, and blue. The sign will hang on the outside of the new motel. Include the phone number and website. 512-903-4417 harborlodgehub.org
I have attached the original sign that this will replace and also an idea of the american flag in the background of the words.

Target Market(s)

This will be seen by people driving by the non profit.

Industry/Entity Type

Non Profit

Logo Text

Harbor Lodge

Font styles to use
Other font styles liked:
• Black Ops One (or similar)

Colors
0355a3
ec1f27

Requirements
Must have
• Colors should be patriotic to the United States. This will need to have font that can be seen while driving.
Nice to have
• Somehow incorporate the American Flag or something patriotic.
Should not have
• Should not have very thin font.

```html
<!DOCTYPE html>
<html lang="en">
<head>
<meta charset="utf-8">
<title>Harbor Lodge – Road Sign</title>
<link href="https://fonts.googleapis.com/css2?family=Black+Ops+One&family=Orbitron:wght@500&display=swap" rel="stylesheet">
<style>
  :root {
    --stage: #e6e8eb;
    --sign-white: #ffffff;
    --flag-blue: #0355a3;
    --flag-red: #ec1f27;
    --edge-grey: #5e5e5e;
  }
  html, body {
    margin: 0;
    padding: 0;
    width: 1200px;
    height: 894px;
    overflow: hidden;
    background: var(--stage);
  }
  .sign {
    position: absolute;
    left: 210px;
    top: 53px;
    width: 780px;
    height: 787px;
    background: var(--sign-white);
    border-bottom: 5px solid var(--edge-grey);
    box-sizing: border-box;
    overflow: hidden;
  }
  .flag-art {
    position: absolute;
    left: 0;
    top: 0;
    width: 780px;
    height: 400px;
  }
  .rating-stars {
    position: absolute;
    left: 410px;
    top: 376px;
    width: 330px;
    height: 50px;
  }
  .lodge-name {
    position: absolute;
    right: 44px;
    top: 446px;
    margin: 0;
    font-family: "Black Ops One", sans-serif;
    font-weight: 400;
    font-size: 86px;
    line-height: 1;
    color: var(--flag-blue);
    white-space: nowrap;
  }
  .contact {
    position: absolute;
    right: 46px;
    top: 596px;
    margin: 0;
    text-align: right;
    font-family: "Orbitron", sans-serif;
    font-weight: 500;
    color: var(--flag-red);
    line-height: 1;
    white-space: nowrap;
  }
  .contact .phone {
    display: block;
    font-size: 76px;
  }
  .contact .website {
    display: block;
    margin-top: 4px;
    font-size: 58px;
  }
</style>
</head>
<body>
  <main class="sign">
    <svg class="flag-art" viewBox="0 0 780 400" role="img" aria-label="Waving American flag illustration in red, white and blue">
      <path d="M0 0 H780 V220 C700 240 620 250 520 262 C400 276 320 300 230 330 C140 360 60 378 0 398 Z" fill="#ec1f27"/>
    </svg>

    <svg class="rating-stars" viewBox="0 0 330 50" aria-hidden="true">
      <g fill="#ec1f27">
        <polygon points="25,2 31,19 49,19 34,30 40,48 25,37 10,48 16,30 1,19 19,19"/>
        <polygon transform="translate(70 0)" points="25,2 31,19 49,19 34,30 40,48 25,37 10,48 16,30 1,19 19,19"/>
        <polygon transform="translate(140 0)" points="25,2 31,19 49,19 34,30 40,48 25,37 10,48 16,30 1,19 19,19"/>
        <polygon transform="translate(210 0)" points="25,2 31,19 49,19 34,30 40,48 25,37 10,48 16,30 1,19 19,19"/>
        <polygon transform="translate(280 0)" points="25,2 31,19 49,19 34,30 40,48 25,37 10,48 16,30 1,19 19,19"/>
      </g>
    </svg>

    <h1 class="lodge-name">Harbor Lodge</h1>

    <p class="contact">
      <span class="phone">512-903-4417</span>
      <span class="website">harborlodgehub.org</span>
    </p>
  </main>
</body>
</html>
```